Velanqua Cookbook (Independant Velanqua Consultant - not Velanqua themselves)

Approx 120 page Recipe book, need design created for recipe pages.
each recipe illustrated with full colour photograph (supplied) on opposite page.
To included index, contents page, intro, etc
Cover design also to be suggested.
We must have a professional finish, but with a friendly, family theme.
Reason: Deadline extended because I require further designs, please.

```html
<!DOCTYPE html>
<html lang="en">
<head>
<meta charset="utf-8">
<title>Steamed Trout with Parsley Butter – Velanqua Cookbook</title>
<link rel="stylesheet" href="https://fonts.googleapis.com/css2?family=Cormorant+SC:wght@500;600;700&family=Kaushan+Script&display=block">
<style>
  :root {
    --paper: #ffffff;
    --ink: #2a2a2a;
    --teal: #3f6b68;
    --band: #456e6b;
    --sage: #8fa35f;
    --rose: #a9636a;
    --dot: #ddd2bd;
    --photo-light: #b3a89b;
    --photo-dark: #8f857a;
    --veil: rgba(255, 255, 255, 0.35);
  }
  * { margin: 0; padding: 0; box-sizing: border-box; }
  html, body { width: 1200px; height: 600px; overflow: hidden; background: var(--paper); }
  .spread { position: relative; width: 1200px; height: 600px; font-family: "Cormorant SC", Georgia, serif; color: var(--ink); }

  .recipe-page { position: absolute; left: 0; top: 0; width: 446px; height: 600px; background: var(--paper); }
  .recipe-title {
    position: absolute; left: 0; top: 16px; width: 446px; text-align: center;
    font-family: "Kaushan Script", cursive; font-weight: 400; font-size: 20px;
    letter-spacing: 0.5px; color: var(--teal); white-space: nowrap;
  }
  .recipe-title .recipe-title__joiner { font-size: 18px; }

  .column { position: absolute; text-align: center; font-size: 12px; line-height: 15.2px; font-weight: 600; }
  .column--ingredients { left: 12px; width: 210px; top: 131px; }
  .column--method { left: 258px; width: 184px; top: 100px; }

  .section-heading { font-size: 14.5px; font-weight: 700; line-height: 18px; margin-bottom: 4px; color: var(--ink); }
  .section-heading--accent { color: var(--teal); font-weight: 600; }
  .ingredient-list { list-style: none; font-style: italic; font-weight: 700; }
  .plain-list { list-style: none; }
  .column--ingredients .section-heading--accent { margin-top: 30px; }
  .column--method .section-heading--accent { margin-top: 16px; }

  .dot-rule { position: absolute; left: 214px; top: 101px; width: 6px; }
  .dot-rule span { display: block; width: 6px; height: 6px; border-radius: 50%; background: var(--dot); margin-bottom: 13.2px; }

  .diet-tags { position: absolute; left: 190px; top: 490px; display: flex; gap: 5px; }
  .diet-tag {
    width: 22px; height: 22px; border-radius: 50%; color: #fff;
    font-family: Georgia, serif; font-size: 9.5px; line-height: 22px; text-align: center;
  }
  .diet-tag--v { background: var(--teal); }
  .diet-tag--gf { background: var(--sage); }
  .diet-tag--ef { background: var(--rose); }

  .footer-band { position: absolute; left: 0; top: 537px; width: 446px; height: 50px; background: var(--band); }

  .photo-page {
    position: absolute; left: 446px; top: 0; width: 754px; height: 600px;
    background: linear-gradient(160deg, var(--photo-light) 0%, var(--photo-dark) 100%);
  }
  .photo-veil { position: absolute; left: 446px; top: 0; width: 154px; height: 600px; background: var(--veil); }
</style>
</head>
<body>
<main class="spread">
  <section class="recipe-page">
    <h1 class="recipe-title">STEAMED TROUT <span class="recipe-title__joiner">with</span> PARSLEY BUTTER</h1>

    <div class="column column--ingredients">
      <h2 class="section-heading">Ingredients</h2>
      <ul class="ingredient-list">
        <li>1 trout</li>
        <li>½ lemon</li>
        <li>2 cloves garlic</li>
        <li>Salt and pepper</li>
        <li>Parsley butter</li>
      </ul>
      <h2 class="section-heading section-heading--accent">Home Made Parsley Butter</h2>
      <ul class="plain-list">
        <li>60g butter</li>
        <li>1 teaspoon lemon rind, grated</li>
        <li>1 tablespoon parsley</li>
        <li>1 tablespoon lemon juice</li>
      </ul>
    </div>

    <div class="dot-rule" aria-hidden="true">
      <span></span><span></span><span></span><span></span><span></span><span></span><span></span><span></span><span></span><span></span><span></span><span></span><span></span><span></span>
    </div>

    <div class="column column--method">
      <h2 class="section-heading">Step-by-step Instructions</h2>
      <ol class="plain-list">
        <li>Slice lemon.</li>
        <li>Peel and chop garlic.</li>
        <li>Fill trout with lemon, garlic,<br>salt and pepper.</li>
        <li>Place in Steamora tray.</li>
        <li>Fill bowl with 700g water.</li>
        <li>Steam 20 minutes, Steamora<br>temperature, Speed 4.</li>
        <li>Serve with Parsley Butter.</li>
      </ol>
      <h2 class="section-heading section-heading--accent">Home Made Parsley Butter</h2>
      <p>Place all ingredients in clean,<br>dry bowl and mix for 15<br>seconds, Speed 5.<br>Roll into logs and refrigerate,<br>or just place in small dish to<br>serve.</p>
    </div>

    <div class="diet-tags">
      <span class="diet-tag diet-tag--v">V</span>
      <span class="diet-tag diet-tag--gf">GF</span>
      <span class="diet-tag diet-tag--ef">EF</span>
    </div>

    <div class="footer-band"></div>
  </section>

  <div class="photo-page" role="img" aria-label="Photograph of steamed whole trout on lettuce with lemon slices on a white plate, two raw trout and a dish of parsley butter on a wooden table"></div>
  <div class="photo-veil" aria-hidden="true"></div>
</main>
</body>
</html>
```